Postcard Design www.steadfieldclaimsdesk.com

We need a new postcard design that would show our over 25 years of knowledge and expertise, yet touch on the functions and services we can perform, in Medical Billing. The problem is that the competition is fierce, with many many new Medical Billing Companies getting in the act. Unfortunately these companies can be extremely hurtful to the financial well being of medical providers, as they do not know the laws, regulations, nor have the expertise.
Updates

I just received my final approval on my trademark, so the phrase Where Patience Pays & Precision Prevails is now a registered trademark. Also I just realized on my original postcard there is a typo. It should read Over 25 years in claims, billing, and revenue recovery, the "the" should not be there. Also I would like the "free 10 chart/EOB audit" to be a bigger deal that would catch the readers eye, maybe an expiration date or some other "call to action"

Target Market(s)

Target business is medical professionals. Chiropractors, Home Health providers, providers that would have large insurance clientele (Vitacover, PPO).
NOT targeting Familiy Practice, Pediatricians, Hospitals, Dentists.

Industry/Entity Type

Financial

Font styles to use
Serif
Sans Serif

Colors
ec1f27
3277b5
ffffff

Requirements
Must have
• New ideas not just copied from my existing postcard. Something that somehow tells the story of going with inexperience can cost you.

```html
<!DOCTYPE html>
<html lang="en">
<head>
<meta charset="UTF-8">
<title>Steadfield Claims Billing &amp; Audit — Postcard</title>
<link href="https://fonts.googleapis.com/css2?family=Libre+Baskerville:wght@700&family=PT+Sans:ital,wght@0,400;0,700;1,400;1,700&display=swap" rel="stylesheet">
<style>
  :root {
    --brand-blue: #3277b5;
    --deep-blue: #1d4f8f;
    --navy: #163c73;
    --brand-red: #ec1f27;
    --dark-red: #b5141b;
    --white: #ffffff;
    --ink: #111111;
    --url-yellow: #f4e04d;
    --phone-yellow: #ffe23a;
    --gold: #f0b429;
    --gold-dark: #c98a12;
    --coin-green: #8fc65a;
    --paper: #f4f5f7;
  }
  * { margin: 0; padding: 0; box-sizing: border-box; }
  html, body { width: 1200px; height: 750px; overflow: hidden; background: var(--white); }
  .postcard {
    position: relative; width: 1200px; height: 750px; overflow: hidden;
    background: linear-gradient(180deg, var(--white) 0%, var(--paper) 100%);
    font-family: "PT Sans", Arial, sans-serif;
  }

  /* Header band */
  .header {
    position: absolute; left: 0; top: 0; width: 1200px; height: 230px;
    background: linear-gradient(180deg, var(--brand-blue) 0%, var(--deep-blue) 100%);
  }
  .url-tab {
    position: absolute; left: 565px; top: 0; width: 635px; height: 60px;
    background: var(--navy);
    clip-path: polygon(30px 0, 100% 0, 100% 100%, 0 100%);
    color: var(--url-yellow); font-size: 26px; letter-spacing: 1px;
    display: flex; align-items: center; justify-content: center;
  }
  .logo-box {
    position: absolute; left: 13px; top: 19px; width: 248px; height: 196px;
    background: var(--white); border-radius: 18px 0 18px 0;
    display: flex; align-items: center; justify-content: center; gap: 10px;
  }
  .logo-dot { width: 18px; height: 18px; border-radius: 50%; background: var(--brand-red); }
  .logo-name { font-family: "Libre Baskerville", Georgia, serif; font-weight: 700; font-size: 30px; color: var(--brand-red); }
  .company-name {
    position: absolute; left: 289px; top: 48px;
    font-family: "Libre Baskerville", Georgia, serif; font-weight: 700;
    font-size: 46px; line-height: 56px; color: var(--white); text-transform: uppercase;
  }
  .tagline-strip {
    position: absolute; left: 261px; top: 175px; width: 620px; height: 44px;
    background: var(--navy);
    clip-path: polygon(0 0, 100% 0, 96% 100%, 0 100%);
    color: var(--white); font-family: "Libre Baskerville", Georgia, serif; font-weight: 700;
    font-size: 20px; display: flex; align-items: center; padding-left: 28px;
  }
  .tagline-strip sup { font-size: 11px; margin-left: 2px; }
  .experience-seal { position: absolute; left: 963px; top: 55px; }

  /* Main message */
  .money-art {
    position: absolute; left: 60px; top: 240px; width: 160px; height: 122px;
    background: linear-gradient(135deg, var(--coin-green) 0%, var(--gold) 70%, var(--gold-dark) 100%);
    border-radius: 24px;
  }
  .headline {
    position: absolute; left: 234px; top: 268px;
    font-weight: 700; font-size: 37px; line-height: 51px; color: var(--ink);
  }
  .pitch { position: absolute; left: 0; top: 385px; }
  .pitch-line {
    position: relative; font-weight: 700; font-style: italic; font-size: 27px;
    color: var(--ink); height: 50px; line-height: 40px; padding-left: 108px; white-space: nowrap;
  }
  .pitch-line.continued { margin-top: -8px; padding-left: 22px; }
  .tick-flag {
    position: absolute; left: 22px; top: 6px; width: 70px; height: 30px;
    background: var(--dark-red);
    clip-path: polygon(0 0, 100% 0, 88% 100%, 0 100%);
  }
  .tick-flag svg { position: absolute; left: 30px; top: 3px; }

  /* Experience + audit offer panel */
  .offer-panel {
    position: absolute; left: 828px; top: 230px; width: 372px; height: 248px;
    background: linear-gradient(180deg, var(--deep-blue) 0%, var(--navy) 100%);
    clip-path: polygon(0 0, 100% 0, 100% 100%, 5% 100%, 0 92%);
    color: var(--white); text-align: right;
    padding: 18px 26px 0 20px;
  }
  .experience-text {
    font-size: 19px; line-height: 23px;
    padding-bottom: 12px; border-bottom: 2px solid rgba(255,255,255,.8); margin-left: 10px;
  }
  .audit-offer { padding-top: 9px; }
  .audit-lead { font-size: 19px; line-height: 22px; }
  .audit-title {
    font-weight: 700; font-size: 31px; line-height: 34px; color: var(--phone-yellow);
    text-transform: uppercase;
  }
  .audit-value { font-size: 18px; line-height: 22px; }
  .audit-deadline {
    display: inline-block; margin-top: 6px; padding: 2px 10px;
    background: var(--brand-red); font-weight: 700; font-size: 17px; line-height: 22px;
  }

  .call-out {
    position: absolute; left: 510px; top: 539px; width: 690px; height: 62px;
    background: var(--brand-blue); border-radius: 18px 0 0 18px;
    color: var(--white); font-style: italic; font-size: 21px; line-height: 26px;
    text-align: center; padding-top: 5px;
  }

  /* Footer */
  .footer { position: absolute; left: 0; top: 600px; width: 1200px; height: 150px; }
  .footer-wave { position: absolute; left: 0; top: 0; }
  .footer-text { position: absolute; left: 0; top: 0; width: 1200px; text-align: center; }
  .address {
    position: absolute; left: 0; width: 1200px; top: 52px;
    color: var(--white); font-style: italic; font-weight: 700; font-size: 22px;
  }
  .phones {
    position: absolute; left: 0; width: 1200px; top: 84px;
    color: var(--phone-yellow); font-style: italic; font-weight: 700; font-size: 31px;
  }
</style>
</head>
<body>
<main class="postcard">
  <header class="header">
    <div class="url-tab">www.steadfieldclaimsdesk.com</div>
    <div class="logo-box"><span class="logo-dot"></span><span class="logo-name">Steadfield</span></div>
    <h1 class="company-name">Steadfield Claims<br>Billing &amp; Audit</h1>
    <div class="tagline-strip">Where Patience Pays &amp; Precision Prevails<sup>®</sup></div>
    <svg class="experience-seal" width="160" height="150" viewBox="0 0 160 150" role="img" aria-label="Gold 25 years experience seal">
      <circle cx="80" cy="75" r="72" fill="var(--gold)"/>
      <circle cx="80" cy="75" r="54" fill="var(--gold-dark)"/>
      <circle cx="80" cy="75" r="44" fill="#2a2a2a"/>
    </svg>
  </header>

  <div class="money-art" role="img" aria-label="Stack of gold coins and dollar bills"></div>

  <h2 class="headline">HOW MUCH MONEY IS<br>HIDING IN YOUR CHARTS?</h2>

  <div class="pitch">
    <p class="pitch-line">Let me recover your lost/ hidden profits!</p>
    <p class="pitch-line"><span class="tick-flag"><svg width="26" height="24" viewBox="0 0 26 24"><path d="M3 12 L10 19 L23 4" stroke="var(--phone-yellow)" stroke-width="5" fill="none" stroke-linecap="round"/></svg></span>guaranteed methods to increase your collectibles.</p>
    <p class="pitch-line"><span class="tick-flag"><svg width="26" height="24" viewBox="0 0 26 24"><path d="M3 12 L10 19 L23 4" stroke="var(--phone-yellow)" stroke-width="5" fill="none" stroke-linecap="round"/></svg></span>Let me turn your denied/ delayed claims into</p>
    <p class="pitch-line continued">Cash in to your Pockets!</p>
  </div>

  <aside class="offer-panel">
    <p class="experience-text">Over 25 years in claims, billing, and revenue recovery; PPO, HMO, Vitacover</p>
    <div class="audit-offer">
      <p class="audit-lead">Call me today for a</p>
      <p class="audit-title">FREE 10-Chart/EOB Audit</p>
      <p class="audit-value">($500.00 - $1200.00 Value)</p>
      <p class="audit-deadline">Offer ends 12/31 — call now!</p>
    </div>
  </aside>

  <div class="call-out">Inexperienced billers cost you money you never see...<br>Don't let those claims go to waste. I can go get them!</div>

  <footer class="footer">
    <svg class="footer-wave" width="1200" height="150" viewBox="0 0 1200 150">
      <path d="M0 40 Q600 -10 1200 40 L1200 150 L0 150 Z" fill="var(--dark-red)"/>
      <path d="M0 48 Q600 2 1200 48 L1200 150 L0 150 Z" fill="var(--brand-red)"/>
    </svg>
    <div class="footer-text">
      <p class="address">4870 Larkspur Ave, # 210-318, Fernhollow, CA 90000</p>
      <p class="phones">Toll free(844) Stead-Fd (555-0142) Fax (844) 555-0143</p>
    </div>
  </footer>
</main>
</body>
</html>
```